Visualisation Software brochure

i need a sales brochure for a new visualisation software company called Lumora Scene Studio.
The software has been specifically designed for manufacturers, distributers and retailers in the design / décor / furnishing / building industries. It allows customers can then import unlimited numbers of digital photos of rooms from their own home or take advantage of a library of pre-made photos, and then render different products from your catalogue into that photo to see what the finished look will be.
i have attached:
1) a mock up of the home page of the website
2) example of brochure wording that i have put together (although i am a little unsure about what other words i can add - so any suggestions here would be good)
3) i have attached some examples of other brochures that i like and would like similar designs
I am after a classy brochure used by a large corporate technology company that is given to executives and gives an impression of quality, trustworthiness and innovation.
• the colour blue as per the colours on my website mock up provided in the design brief
• I like simple, smart, clean and uncluttered design
• I like simple, clean and uncluttered design
• I like pictures that fit in with my technology (whether that be home and interior design, mixing virtual world and real world, visualising an idea) rather than basic stock of corporate people
Updates
Target Market(s)
marketing professionals
Industry/Entity Type
Software
Font styles to use
Look and feel
Each slider illustrates characteristics of the customer's brand and the style your logo design should communicate.

```html
<!DOCTYPE html>
<html lang="en">
<head>
<meta charset="utf-8">
<title>Lumora Scene Studio – Brochure</title>
<link rel="stylesheet" href="https://fonts.googleapis.com/css2?family=Roboto+Condensed:wght@700&family=Open+Sans:wght@400&family=Raleway:wght@400&display=swap">
<style>
  :root{
    --backdrop:#8b5e3c;
    --ink-dark:#1d2229;
    --ink-dark-2:#242a32;
    --paper:#e3e1dc;
    --paper-2:#d9d6cf;
    --text-dark:#2a2a2a;
    --text-body:#4a4a4a;
    --text-light:#ffffff;
    --text-muted:#d8dbe0;
    --brand-blue:#2f5fc4;
    --bevel:#b9b9b9;
  }
  *{margin:0;padding:0;box-sizing:border-box}
  html,body{width:1200px;height:864px;overflow:hidden;background:var(--backdrop)}
  .spread{position:absolute;left:90px;top:69px;width:1023px;height:728px;background:var(--paper)}
  .panel{position:absolute}
  .contact-band{left:0;top:0;width:511px;height:101px;background:var(--ink-dark);color:var(--text-light);text-align:center}
  .phone{font:700 29px/1 "Roboto Condensed",sans-serif;padding-top:30px}
  .website{font:400 14px/1 "Open Sans",sans-serif;letter-spacing:2.4px;margin-top:11px}
  .brand-band{left:512px;top:0;width:511px;height:101px;background:var(--paper);display:flex;align-items:center;justify-content:center;gap:12px}
  .brand-dot{width:46px;height:46px;border-radius:50%;background:var(--brand-blue)}
  .brand-dot.small{width:38px;height:38px}
  .brand-name{font:400 21px/1 "Raleway",sans-serif;color:var(--text-dark)}
  .brand-name.light{color:var(--text-light);font-size:17px}
  .photo{top:103px;height:386px;border-top:3px solid var(--bevel);border-bottom:3px solid var(--bevel)}
  .photo-bathroom{left:0;width:511px;background:linear-gradient(160deg,#f4f4f2 0%,#d9d9d6 45%,#8f8f8c 75%,#c9b08c 100%)}
  .photo-kitchen{left:512px;width:511px;background:linear-gradient(170deg,#c9c3b4 0%,#8a6a4c 35%,#4e3422 70%,#2c1d14 100%)}
  .about{left:0;top:491px;width:511px;height:237px;background:var(--ink-dark-2);color:var(--text-light);text-align:center}
  .about .logo-row{display:flex;justify-content:center;align-items:center;gap:10px;margin-top:26px}
  .about h2{font:700 17px/1 "Roboto Condensed",sans-serif;margin-top:42px}
  .about p{font:400 8.4px/1.45 "Open Sans",sans-serif;color:var(--text-muted);width:410px;margin:14px auto 0}
  .intro{left:512px;top:491px;width:511px;height:237px;background:linear-gradient(var(--paper),var(--paper-2))}
  .intro h2{position:absolute;left:30px;top:20px;font:700 16px/1 "Roboto Condensed",sans-serif;color:var(--text-dark)}
  .intro .copy{position:absolute;left:30px;top:48px;width:242px;font:400 8.2px/1.42 "Open Sans",sans-serif;color:var(--text-body)}
  .intro .copy p+p{margin-top:11px}
  .divider{position:absolute;left:296px;top:28px;width:1px;height:188px;background:#a9a6a0}
  .tagline-col{position:absolute;left:305px;top:32px;width:200px;text-align:center}
  .tagline-col .logo-row{display:flex;justify-content:center}
  .tagline{font:700 26px/1.1 "Roboto Condensed",sans-serif;color:var(--text-dark);margin-top:22px}
</style>
</head>
<body>
<main class="spread">
  <header class="panel contact-band">
    <div class="phone">+61 (0) 400 555 018</div>
    <div class="website">WWW.LUMORASCENES.COM</div>
  </header>
  <div class="panel brand-band">
    <span class="brand-dot"></span>
    <span class="brand-name">Lumora Scene Studio</span>
  </div>

  <div class="panel photo photo-bathroom" role="img" aria-label="Rendered modern bathroom with twin basins, mirror and heated towel rail"></div>
  <div class="panel photo photo-kitchen" role="img" aria-label="Rendered timber kitchen with dining table, chairs and a tablet showing the visualiser app"></div>

  <section class="panel about">
    <div class="logo-row"><span class="brand-dot small"></span><span class="brand-name light">Lumora Scene Studio</span></div>
    <h2>About Lumora Scene Studio</h2>
    <p>Formed in 2013 based on a growing need in the market for a fully functional tool. Many other products offer big promises but their short comings impede the success of the retailers. Our goal is to ensure a premium experience for customers and retailers. We are very focused to be the obvious leader in this space. This is based upon our 12 point methodology to maximise customer satisfaction to 95% percentile and beyond.</p>
  </section>

  <section class="panel intro">
    <h2>Innovation redefining retail</h2>
    <div class="copy">
      <p>We have a product that is rapidly being seen as the next market leader in interactive visualisation software. Lumora Scene Studio has been developed as an all-inclusive, easy-to-use solution that has been specifically designed for retail businesses within the design, décor, flooring, furnishing, building/renovation and real estate industries.</p>
      <p>Lumora Scene Studio is an innovative and powerful web and/or app-based platform that delivers you the capability to positively transform the overall retail experience of your customers as well as your bottom-line as it helps your customers achieve results by being able to visualise and conceptualise in real time how wonderful their real rooms or new homes could look with your products.</p>
    </div>
    <div class="divider"></div>
    <div class="tagline-col">
      <div class="logo-row"><span class="brand-dot small"></span></div>
      <p class="tagline">Leading the<br>way in<br>visualisation<br>software</p>
    </div>
  </section>
</main>
</body>
</html>
```